KTVance Auctions on responsive WP

We need a wordpress design for an established auction and real estate company based in South Carolina. The winning design will incorporate a professional color scheme with company logo in a clean layout. The design needs to consider that this will be developed on a responsive theme. Colors are those that will highlight the logo.

Industry/Entity Type

Real Estate

Font styles to use
Serif
Sans Serif

Colors

Designer to choose colors to be used in the design.

Requirements
Must have
• Colors will be black, dark gray and red. A dark color scheme is ok. They like marlowick.net as a layout. Site tagline - "Auctioneers & Appraisers Since 1977" Site will have slideshow, please use stock photo for the initial image.

- navigation: 1) home 2) Auctions 3) For Sale 4) Buyers & Sellers 5) FAQ 6) About Us 7) Links 8) Contact Us

Widgets - 1) Join Our Email List 2) Social media icons (FB, twitter, RSS) 3) Featured Auctions 4) News & Events blog

footer will have smaller company logo, contact info (below) and attached association logos.
Phone: (803) 555-0147
Contacts: Derek Vance
Email: derek@ktvance-example.com
Address: 482 North Birchfield (Hwy. 61), Ridgeway, SC 29130
Nice to have
• Use and style of a dropmenu - Under AUCTIONS 1) upcoming auctions 2) past auctions

```html
<!DOCTYPE html>
<html lang="en">
<head>
<meta charset="utf-8">
<title>KTVance Auctions</title>
<link href="https://fonts.googleapis.com/css2?family=Open+Sans:ital,wght@0,400;0,600;0,700;1,400&family=Noto+Serif:wght@700&display=swap" rel="stylesheet">
<style>
:root{
  --red:#d8142a;
  --navy:#1d3a5c;
  --ink:#222;
  --text:#333;
  --muted:#666;
  --rule:#d8d8d8;
  --dark:#111;
  --footer:#ececec;
  --date:#3a3f44;
}
*{margin:0;padding:0;box-sizing:border-box}
html,body{width:952px;height:1200px;overflow:hidden;background:#fff}
body{position:relative;font-family:"Open Sans",sans-serif;color:var(--text)}
.abs{position:absolute}

.brand{left:100px;top:20px;display:flex;align-items:center;gap:8px}
.brand-mark{width:14px;height:14px;background:var(--red)}
.brand-name{font-family:"Noto Serif",serif;font-weight:700;font-size:23px;color:var(--navy);white-space:nowrap}

.search{left:701px;top:26px;width:151px;height:17px;display:flex}
.search-input{flex:1;border:1px solid #ccc;font-size:8px;font-style:italic;color:#999;padding:2px 4px;line-height:11px}
.search-btn{width:32px;background:#3a3f44;display:flex;align-items:center;justify-content:center}
.follow{left:700px;top:59px;display:flex;align-items:center;gap:4px}
.follow-label{font-size:14px;color:var(--ink);margin-right:4px}
.social{width:21px;height:21px;background:var(--dark);display:flex;align-items:center;justify-content:center}

.nav-top{left:100px;top:91px;width:752px;height:3px;background:var(--dark)}
.nav-bottom{left:100px;top:123px;width:752px;height:1px;background:var(--rule)}
.nav{top:101px;left:0;font-family:"Noto Serif",serif;font-weight:700;font-size:14.6px;color:var(--navy)}
.nav a{position:absolute;white-space:nowrap;text-decoration:none;color:inherit}
.nav-active{left:212px;top:91px;width:78px;height:3px;background:var(--red)}
.dropdown{left:212px;top:124px;width:116px;height:58px;background:#fff;box-shadow:0 1px 4px rgba(0,0,0,.25)}
.dropdown div{font-size:7.5px;color:#444;padding:0 7px;height:21px;line-height:21px}
.dropdown div+div{border-top:1px solid #e5e5e5}

.slider{left:100px;top:138px;width:752px;height:297px;background:linear-gradient(180deg,#b9d6ee 0%,#d9e4ea 30%,#c65a36 38%,#e9dfcc 60%,#8b8a6a 85%,#4f6b31 100%)}
.slider-shadow{left:110px;top:433px;width:732px;height:26px;background:radial-gradient(ellipse at top,rgba(0,0,0,.22),rgba(0,0,0,0) 70%)}
.caption{left:582px;top:228px;width:270px;height:154px;background:rgba(40,35,35,.72)}
.caption-title{left:612px;top:236px;font-size:20px;font-weight:600;color:#fff;white-space:nowrap}
.caption-text{left:614px;top:267px;width:225px;font-size:12.4px;line-height:18px;color:#eee}
.btn-red{background:var(--red);color:#fff;display:flex;align-items:center;justify-content:center;white-space:nowrap}
.caption-btn{left:657px;top:344px;width:109px;height:30px;font-size:15px}
.dots{left:463px;top:415px;width:34px;height:10px;background:#fff;border-radius:5px;display:flex;align-items:center;justify-content:center;gap:2px}
.dots span{width:5px;height:5px;border-radius:50%;background:#333}

.h2{font-size:20px;font-weight:600;color:var(--ink);white-space:nowrap}
.welcome-body{left:100px;top:513px;width:470px;font-size:14.6px;line-height:25.6px;color:var(--text)}

.news-month{font-size:12.5px;color:#e0581f}
.news-day{width:24px;height:19px;background:var(--date);color:#fff;font-size:12px;font-weight:600;text-align:center;line-height:19px}
.news-text{white-space:nowrap;font-size:10.6px;line-height:16px;color:#444}
.news-text .more{color:#e0581f}
.news-rule{left:612px;top:577px;width:240px;border-top:1px dashed #bbb}

.card{width:215px;height:161px;border:3px solid #dcdcdc;background:#fff}
.card-photo{left:7px;top:9px;width:83px;height:64px;background:linear-gradient(180deg,#a7c4dc 0%,#6f7680 45%,#d8d6d0 75%,#6a8a45 100%)}
.card-title{left:94px;top:17px;font-size:9.8px;color:var(--red);white-space:nowrap}
.card-list{left:97px;top:34px;font-size:7.6px;line-height:15.3px;color:#666}
.mini-btn{height:9px;background:#3a4a5a;color:#fff;font-size:4px;line-height:9px;text-align:center;border-radius:2px}
.card-meta{left:8px;top:124px;font-size:4.8px;line-height:8.4px;color:#666;white-space:nowrap}
.card-btn{left:96px;top:117px;width:100px;height:24px;font-size:8.8px;font-weight:700;box-shadow:0 1px 1px rgba(0,0,0,.3)}

.pager{top:920px;height:23px;border:1px solid #e2e2e2;background:#fafafa;font-size:10.5px;color:#444;display:flex;align-items:center;justify-content:center}
.pager.current{background:var(--red);color:#fff;border-color:var(--red)}

.feat-photo{top:736px;width:107px;height:75px;background:linear-gradient(180deg,#8fb8dc 0%,#c9b893 40%,#f1ede2 62%,#6f8d3e 88%,#b66a2e 100%)}
.view-more{left:696px;top:826px;width:70px;height:25px;font-size:8.6px;font-weight:700}

.footer{left:0;top:983px;width:952px;height:185px;background:var(--footer);border-top:1px solid #d0d0d0}
.footer-brand{left:123px;top:1010px;display:flex;align-items:center;gap:6px}
.footer-brand .brand-name{font-size:17px}
.footer-brand .brand-mark{width:11px;height:11px}
.contact{left:126px;top:1061px;font-size:10.6px;line-height:18.6px;color:#333}
.foot-h{font-size:13.8px;color:#222;white-space:nowrap}
.email-input{left:377px;top:1043px;width:186px;height:30px;background:#fff;border:1px solid #ccc;font-size:11px;font-style:italic;color:#999;padding:0 12px;line-height:28px}
.signup{left:379px;top:1094px;width:75px;height:28px;font-size:15px}
.assoc{left:654px;top:1040px;width:175px;height:40px;background:#fff;display:flex;align-items:center;justify-content:space-around;padding:0 6px}
.badge{height:24px;background:#2a2a2a}
.copybar{left:0;top:1168px;width:952px;height:32px;background:var(--dark);color:#ddd;font-size:7.6px;text-align:center;line-height:32px}
</style>
</head>
<body>

<header>
  <div class="abs brand"><span class="brand-mark"></span><span class="brand-name">KTVance Auctions</span></div>
  <div class="abs search">
    <div class="search-input">Search item</div>
    <div class="search-btn"><svg width="11" height="9" viewBox="0 0 11 9"><circle cx="4" cy="3.5" r="2.6" fill="none" stroke="#fff" stroke-width="1.3"/><line x1="6" y1="5.3" x2="9.5" y2="8" stroke="#fff" stroke-width="1.6"/></svg></div>
  </div>
  <div class="abs follow">
    <span class="follow-label">Follows Us</span>
    <span class="social" aria-label="News feed"><svg width="11" height="11" viewBox="0 0 11 11"><circle cx="2" cy="9" r="1.5" fill="#fff"/><path d="M1 5a5 5 0 0 1 5 5M1 1a9 9 0 0 1 9 9" fill="none" stroke="#fff" stroke-width="1.6"/></svg></span>
    <span class="social" aria-label="Social profile"><svg width="10" height="10"><rect x="3" y="2" width="4" height="4" fill="#fff"/></svg></span>
    <span class="social" aria-label="Social updates"><svg width="10" height="10"><circle cx="5" cy="5" r="3" fill="#fff"/></svg></span>
  </div>
</header>

<nav>
  <div class="abs nav-top"></div>
  <div class="abs nav-active"></div>
  <div class="abs nav">
    <a style="left:156px">Home</a>
    <a style="left:220px">Auctions</a>
    <a style="left:303px">For Sale</a>
    <a style="left:381px">Buyers &amp; Sellers</a>
    <a style="left:520px">FAQ</a>
    <a style="left:572px">About Us</a>
    <a style="left:660px">Links</a>
    <a style="left:718px">Contact Us</a>
  </div>
  <svg class="abs" style="left:282px;top:110px" width="5" height="4"><path d="M0 0h5L2.5 3z" fill="#c33"/></svg>
  <div class="abs nav-bottom"></div>
</nav>

<section>
  <div class="abs slider" role="img" aria-label="Stock photo of a stucco house with a red tiled roof and garage under blue sky"></div>
  <svg class="abs" style="left:101px;top:258px" width="18" height="30"><path d="M15 2L3 15l12 13" fill="none" stroke="rgba(255,255,255,.75)" stroke-width="5"/></svg>
  <div class="abs slider-shadow"></div>
  <div class="abs caption"></div>
  <div class="abs caption-title">Pellentesque accumsan</div>
  <div class="abs caption-text">Lorem ipsum is a dummy text only. Dolor sit amet, consectetur adipiscing elit. Nullam felis mauris.</div>
  <div class="abs btn-red caption-btn">Learn more</div>
  <div class="abs dots"><span></span><span></span><span></span><span></span></div>
</section>
<div class="abs dropdown"><div>Upcoming Auctions</div><div>Past Auctions</div></div>

<main>
  <h2 class="abs h2" style="left:100px;top:477px">Welcome to KTVance Auctions</h2>
  <p class="abs welcome-body">Lorem ipsum is a dummy text only. Dolor sit amet, consectetur adipiscing elit. Nullam felis mauris, eleifend ac rhoncus non, lobortis at diam. Pellentesque suscipit nulla sit amet venenatis porttitor. In augue felis, venenatis id auctor a, sagittis non ligula. Vestibulum bibendum, nulla quis viverra pharetra.</p>

  <h2 class="abs h2" style="left:612px;top:473px">Recent news &amp; events</h2>
  <div class="abs news-month" style="left:612px;top:514px">July</div>
  <div class="abs news-day" style="left:613px;top:534px">26</div>
  <p class="abs news-text" style="left:651px;top:510px">Lorem ipsum is a dummy text only.<br>Dolor sit amet, consectetur adipiscing<br>elit. Nullam felis mauris....<span class="more">[Read more]</span></p>
  <div class="abs news-rule"></div>
  <div class="abs news-month" style="left:612px;top:608px">July</div>
  <div class="abs news-day" style="left:613px;top:628px">27</div>
  <p class="abs news-text" style="left:651px;top:604px">Lorem ipsum is a dummy text only.<br>Dolor sit amet, consectetur adipiscing<br>elit. Nullam felis mauris....<span class="more">[Read more]</span></p>

  <h2 class="abs h2" style="left:100px;top:696px">Upcoming Auctions</h2>

  <article class="abs card" style="left:100px;top:738px">
    <div class="abs card-photo" role="img" aria-label="Photo of a grey two-storey house with garage"></div>
    <div class="abs card-title">Pellentesque accumsan</div>
    <div class="abs card-list">•Lorem ipsum<br>•Dolor sit amet,<br>•Nullam felis mauris,<br>•Vestibulum</div>
    <div class="abs mini-btn" style="left:17px;top:84px;width:34px">View details</div>
    <div class="abs mini-btn" style="left:53px;top:84px;width:33px">View gallery</div>
    <div class="abs card-meta">ONLINE BIDDING<br>Began: 07/24/14 at 5:00 PM CDT<br>Ends: 08/25/14 at 8:00 PM CDT</div>
    <div class="abs btn-red card-btn">Click to bid online</div>
  </article>
  <article class="abs card" style="left:334px;top:738px">
    <div class="abs card-photo" role="img" aria-label="Photo of a grey two-storey house with garage"></div>
    <div class="abs card-title">Pellentesque accumsan</div>
    <div class="abs card-list">•Lorem ipsum<br>•Dolor sit amet,<br>•Nullam felis mauris,<br>•Vestibulum</div>
    <div class="abs mini-btn" style="left:17px;top:84px;width:34px">View details</div>
    <div class="abs mini-btn" style="left:53px;top:84px;width:33px">View gallery</div>
    <div class="abs card-meta">ONLINE BIDDING<br>Began: 07/24/14 at 5:00 PM CDT<br>Ends: 08/25/14 at 8:00 PM CDT</div>
    <div class="abs btn-red card-btn">Click to bid online</div>
  </article>

  <div class="abs pager" style="left:99px;width:44px">Prev</div>
  <div class="abs pager current" style="left:149px;width:19px">1</div>
  <div class="abs pager" style="left:173px;width:20px">2</div>
  <div class="abs pager" style="left:198px;width:20px">3</div>
  <div class="abs pager" style="left:224px;width:21px">...</div>
  <div class="abs pager" style="left:250px;width:21px">8</div>
  <div class="abs pager" style="left:278px;width:44px">Next</div>

  <h2 class="abs h2" style="left:615px;top:696px">Featured Auctions</h2>
  <svg class="abs" style="left:840px;top:710px" width="13" height="13"><circle cx="6.5" cy="6.5" r="6" fill="var(--red)"/><path d="M4 6.5h4M6 4.3l2.3 2.2L6 8.7" fill="none" stroke="#fff" stroke-width="1.5"/></svg>
  <div class="abs feat-photo" style="left:619px" role="img" aria-label="Photo of a cream house with a wide front porch"></div>
  <div class="abs feat-photo" style="left:743px" role="img" aria-label="Photo of a cream house with a wide front porch"></div>
  <div class="abs btn-red view-more">View more</div>
</main>

<footer>
  <div class="abs footer"></div>
  <div class="abs footer-brand"><span class="brand-mark"></span><span class="brand-name">KTVance Auctions</span></div>
  <div class="abs contact">Phone: (555) 555-0147<br>Contacts: Derek Vance<br>Email: derek@ktvance-example.com<br>Address: 482 North Birchfield<br>(Hwy. 61), Larkmoor, SC 29999</div>
  <div class="abs foot-h" style="left:378px;top:1013px">Subscribe to our Newsletter</div>
  <div class="abs email-input">Enter your email address</div>
  <div class="abs btn-red signup">Sign Up</div>
  <div class="abs foot-h" style="left:653px;top:1013px">Our Associations</div>
  <div class="abs assoc">
    <span class="badge" style="width:70px"></span>
    <span class="badge" style="width:28px;height:32px"></span>
    <span class="badge" style="width:36px;border-radius:4px"></span>
  </div>
  <div class="abs copybar">Copyright©KTVance &amp;Co. All Rights Reserved</div>
</footer>

</body>
</html>
```